Need a book cover design for a Vellora Book on Herbal Remedies

I need a book cover for my new ebook, here are the details:
Title: Meadow Tonics
Sub-Heading: Old Garden Wisdom Notes
Finding the Quiet Strength of the Wild for Daily Balance and Calm
Author: Mara Delacroix

```html
<!DOCTYPE html>
<html lang="en">
<head>
<meta charset="UTF-8">
<title>Meadow Tonics — Mara Delacroix</title>
<link rel="stylesheet" href="https://fonts.googleapis.com/css2?family=Anton&family=Oswald:wght@600;700&family=Archivo+Narrow:ital,wght@1,500&display=swap">
<style>
  :root {
    --paper: #f4f1ea;
    --herb-green: #4f7a3a;
    --herb-brown: #7a4e2e;
    --herb-dark: #3b2a1e;
    --petal-pink: #c77aa8;
    --petal-blue: #6f76c4;
    --title-wood: #4a2e1c;
    --leaf-green: #3f6b2c;
    --ink: #2f2520;
  }
  * { margin: 0; padding: 0; box-sizing: border-box; }
  html, body { width: 750px; height: 1200px; overflow: hidden; background: var(--paper); }
  .cover {
    position: relative;
    width: 750px;
    height: 1200px;
    overflow: hidden;
  }
  .herb-border {
    position: absolute;
    inset: 0;
    background:
      radial-gradient(ellipse 34% 38% at 50% 47%, var(--paper) 0 82%, rgba(244,241,234,0) 100%),
      radial-gradient(circle at 10% 12%, var(--petal-pink) 0 8%, transparent 14%),
      radial-gradient(circle at 90% 8%, #e9a9bf 0 6%, transparent 12%),
      radial-gradient(circle at 88% 52%, var(--petal-blue) 0 6%, transparent 12%),
      radial-gradient(circle at 12% 55%, #b78cd6 0 6%, transparent 12%),
      radial-gradient(circle at 55% 95%, var(--petal-blue) 0 5%, transparent 11%),
      radial-gradient(circle at 40% 8%, #c4402a 0 5%, transparent 10%),
      linear-gradient(135deg, var(--herb-brown), var(--herb-green) 50%, var(--herb-brown));
  }
  .cover-text {
    position: absolute;
    inset: 0;
    text-align: center;
  }
  .author {
    position: absolute;
    top: 262px;
    left: 0; right: 0;
    font-family: 'Oswald', sans-serif;
    font-weight: 700;
    font-size: 38px;
    letter-spacing: 7px;
    color: var(--leaf-green);
  }
  .title {
    position: absolute;
    top: 340px;
    left: 0; right: 0;
    font-family: 'Anton', sans-serif;
    font-weight: 400;
    font-size: 136px;
    line-height: 142px;
    color: var(--title-wood);
    letter-spacing: 1px;
  }
  .subheading {
    position: absolute;
    top: 640px;
    left: 0; right: 0;
    font-family: 'Oswald', sans-serif;
    font-weight: 700;
    font-size: 50px;
    line-height: 58px;
    color: var(--leaf-green);
    text-transform: uppercase;
  }
  .tagline {
    position: absolute;
    top: 808px;
    left: 0; right: 0;
    font-family: 'Archivo Narrow', sans-serif;
    font-style: italic;
    font-weight: 500;
    font-size: 32px;
    line-height: 44px;
    color: var(--ink);
  }
</style>
</head>
<body>
  <main class="cover">
    <div class="herb-border" role="img" aria-label="Photograph of wooden bowls filled with dried herbs, petals and seeds, with fresh flowers, framing a pale centre"></div>
    <div class="cover-text">
      <p class="author">MARA DELACROIX</p>
      <h1 class="title">Meadow<br>Tonics</h1>
      <h2 class="subheading">Old Garden<br>Wisdom Notes</h2>
      <p class="tagline">Finding the Quiet Strength<br>of the Wild for Daily<br>Balance and Calm</p>
    </div>
  </main>
</body>
</html>
```